kestrova business cards

Hey design gurus!
I'm after a clean, modern, stylish business card for my about to be launched company.
I've uploaded the logos for my company "Kestrova Electrical Solutions"
and also the tarrow alliance logo to whom i am associated.

```html
<!DOCTYPE html>
<html lang="en">
<head>
<meta charset="utf-8">
<title>Kestrova Electrical Solutions – Business Cards</title>
<link href="https://fonts.googleapis.com/css2?family=Montserrat:wght@400;500;700;800&display=swap" rel="stylesheet">
<style>
  :root {
    --stage: #2a2b2d;
    --card: #03141c;
    --card-edge: #0a2430;
    --blue: #1e8ee0;
    --white: #f2f5f7;
    --emboss: #3a4248;
    --rule: #e8edf0;
  }
  * { box-sizing: border-box; margin: 0; padding: 0; }
  html, body { width: 1200px; height: 689px; overflow: hidden; }
  body {
    background: var(--stage);
    font-family: "Montserrat", sans-serif;
    position: relative;
  }
  .card {
    position: absolute;
    top: 190px;
    width: 540px;
    height: 310px;
    border-radius: 26px;
    background: var(--card);
    border: 1px solid var(--card-edge);
    overflow: hidden;
  }
  .card--back { left: 30px; }
  .card--front { left: 630px; }

  /* back side */
  .back-brand {
    position: absolute;
    left: 70px; top: 126px;
    display: flex; align-items: center; gap: 16px;
  }
  .brand-dot {
    width: 52px; height: 52px; border-radius: 50%;
    border: 4px solid currentColor;
  }
  .back-brand { color: var(--emboss); }
  .back-brand .brand-name {
    font-weight: 800; font-size: 24px; letter-spacing: 1px;
    text-transform: uppercase; line-height: 1.1;
  }
  .badge {
    position: absolute;
    right: 34px; top: 38px;
    width: 130px; height: 52px;
    border: 2px solid var(--white);
    border-radius: 6px;
  }
  .badge::before {
    content: "";
    position: absolute; left: 10px; top: 10px;
    width: 28px; height: 28px; background: var(--white); border-radius: 4px;
  }

  /* front side */
  .front-brand {
    position: absolute;
    left: 100px; top: 46px;
    display: flex; align-items: center; gap: 16px;
    color: var(--blue);
  }
  .front-brand .brand-name {
    font-weight: 800; font-size: 24px; letter-spacing: 1px;
    text-transform: uppercase; line-height: 1.1;
  }
  .divider {
    position: absolute; left: 150px; right: 36px; top: 150px;
    height: 1px; background: var(--rule);
  }
  .person { position: absolute; left: 36px; top: 150px; }
  .person-name { color: var(--blue); font-weight: 700; font-size: 28px; line-height: 1.1; }
  .person-role { color: var(--white); font-weight: 500; font-size: 15px; margin-top: 2px; }
  .person-rule { width: 190px; height: 1px; background: var(--rule); margin-top: 10px; }
  .contacts { list-style: none; margin-top: 10px; }
  .contacts li {
    display: flex; align-items: center; gap: 10px;
    color: var(--white); font-size: 14px; font-weight: 400; margin-bottom: 6px;
  }
  .contacts svg { width: 16px; height: 16px; fill: none; stroke: var(--blue); stroke-width: 2; }
  .address {
    position: absolute; right: 36px; top: 176px;
    color: var(--white); font-size: 15px; text-align: right; line-height: 1.45;
  }
</style>
</head>
<body>

<section class="card card--back" aria-label="Business card back">
  <div class="back-brand">
    <span class="brand-dot"></span>
    <span class="brand-name">Kestrova<br>Electrical Solutions</span>
  </div>
  <div class="badge" role="img" aria-label="tarrow alliance membership badge"></div>
</section>

<section class="card card--front" aria-label="Business card front">
  <div class="front-brand">
    <span class="brand-dot"></span>
    <span class="brand-name">Kestrova<br>Electrical Solutions</span>
  </div>
  <div class="divider"></div>

  <div class="person">
    <p class="person-name">Jordan Reyes</p>
    <p class="person-role">Managing Director</p>
    <div class="person-rule"></div>
    <ul class="contacts">
      <li>
        <svg viewBox="0 0 24 24"><path d="M5 3h4l2 5-2.5 1.5a11 11 0 0 0 6 6L16 13l5 2v4a2 2 0 0 1-2 2A16 16 0 0 1 3 5a2 2 0 0 1 2-2z"/></svg>
        (123.456.7890)
      </li>
      <li>
        <svg viewBox="0 0 24 24"><rect x="3" y="5" width="18" height="14" rx="1"/><path d="M3 6l9 7 9-7"/></svg>
        info@webname.com
      </li>
      <li>
        <svg viewBox="0 0 24 24"><circle cx="12" cy="12" r="9"/><path d="M3 12h18M12 3a14 14 0 0 1 0 18M12 3a14 14 0 0 0 0 18"/></svg>
        www.websitename.com
      </li>
    </ul>
  </div>

  <p class="address">425 address line here<br>Country Name 45442</p>
</section>

</body>
</html>
```